FAST TURN AROUND - Yoga & Sound Meditation Event Flyer

Our organization - Tarrow Guidance Alliance - is currently looking for someone to create a flyer for an upcoming Yoga & Sound Meditation Event.

We are looking for the following deliverables:
Versions of the Flyer created for Social Media (Long Story & Square Post) that includes the following information. (Not including the categories)
Event Title: Tarrow Flow & Hum Unwind Session - Bayline Mix
Event Date & Time: Wednesday, April 20 | 7P - 9P
Event Location: Reedhall at Cobbleyard
Tarrow Logo: (Both black and white versions are attached. Feel free to use whichever makes more sense based on the lighting)

We would want a version of this for the eight different background images provided. For the test, you can submit 1-2 since the rest of the details will be the same once we chose the information design.

```html
<!DOCTYPE html>
<html lang="en">
<head>
<meta charset="utf-8">
<title>Tarrow Flow &amp; Hum Unwind Session – Flyers</title>
<link href="https://fonts.googleapis.com/css2?family=Bebas+Neue&family=Montserrat:wght@500;600;700&display=swap" rel="stylesheet">
<style>
  :root {
    --page: #ffffff;
    --photo-deep: #241006;
    --photo-mid: #5a2a0c;
    --photo-glow: #b8621c;
    --panel: #e0e0e0;
    --ink: #111111;
    --light-text: #f3eee8;
    --location-bar: #000000;
  }
  * { margin: 0; padding: 0; box-sizing: border-box; }
  html, body {
    width: 1200px; height: 900px; overflow: hidden;
    background: var(--page);
    font-family: "Montserrat", Arial, sans-serif;
  }
  .flyer {
    position: absolute;
    overflow: hidden;
    background: var(--panel);
    color: var(--ink);
  }
  .flyer--story { left: 112px; top: 129px; width: 359px; height: 637px; }
  .flyer--square { left: 584px; top: 129px; width: 504px; height: 503px; }

  .flyer__photo {
    position: absolute; left: 0; top: 0; width: 100%;
    background:
      radial-gradient(ellipse 55% 40% at 50% 32%, var(--photo-glow) 0%, rgba(184,98,28,0) 100%),
      linear-gradient(180deg, var(--photo-mid) 0%, var(--photo-deep) 65%, #3a1a08 100%);
  }
  .flyer--story .flyer__photo { height: 493px; }
  .flyer--square .flyer__photo { height: 359px; }

  .centered { position: absolute; left: 0; right: 0; text-align: center; }

  .brand__name { font-weight: 700; color: var(--light-text); line-height: 1; letter-spacing: 0.5px; }
  .brand__tagline { font-weight: 500; color: var(--light-text); line-height: 1; }

  .event-title {
    font-family: "Bebas Neue", "Arial Narrow", sans-serif;
    font-weight: 400;
    color: var(--light-text);
    text-transform: uppercase;
  }
  .event-mix {
    font-weight: 500; color: var(--light-text);
    text-transform: uppercase; line-height: 1;
  }
  .event-date { font-weight: 500; text-transform: uppercase; }

  .location-label {
    position: absolute; left: 50%; transform: translateX(-50%);
    border: 1px solid #333; background: var(--panel);
    font-weight: 600; text-transform: uppercase; text-align: center;
    color: #222; white-space: nowrap;
  }
  .location-name {
    position: absolute; left: 50%; transform: translateX(-50%);
    background: var(--location-bar); color: #ffffff;
    font-weight: 700; text-transform: uppercase; text-align: center;
    white-space: nowrap;
  }

  /* Story sizes */
  .flyer--story .brand__name { top: 21px; font-size: 30px; }
  .flyer--story .brand__tagline { top: 52px; font-size: 12px; }
  .flyer--story .event-title { top: 390px; font-size: 36px; line-height: 31px; }
  .flyer--story .event-mix { top: 452px; font-size: 16px; letter-spacing: 3px; }
  .flyer--story .event-date { top: 502px; font-size: 27px; line-height: 27px; }
  .flyer--story .location-label { top: 571px; padding: 0 14px; height: 20px; font-size: 12px; line-height: 18px; letter-spacing: 1px; }
  .flyer--story .location-name { top: 591px; padding: 0 9px 0 10px; height: 32px; font-size: 17px; line-height: 32px; letter-spacing: 1px; }

  /* Square sizes */
  .flyer--square .brand__name { top: 25px; font-size: 33px; }
  .flyer--square .brand__tagline { top: 57px; font-size: 13px; }
  .flyer--square .event-title { top: 233px; font-size: 46px; line-height: 40px; }
  .flyer--square .event-mix { top: 315px; font-size: 20px; letter-spacing: 4px; }
  .flyer--square .event-date { top: 372px; font-size: 26px; line-height: 28px; }
  .flyer--square .location-label { top: 414px; padding: 0 14px; height: 25px; font-size: 15px; line-height: 23px; letter-spacing: 1px; }
  .flyer--square .location-name { top: 440px; padding: 0 11px 0 12.5px; height: 39px; font-size: 21px; line-height: 39px; letter-spacing: 1.5px; }
</style>
</head>
<body>

<section class="flyer flyer--story" aria-label="Story flyer">
  <div class="flyer__photo" role="img" aria-label="Photo: sound healer playing a gong in a warmly lit room with participants resting on mats"></div>
  <p class="brand__name centered">Tarrow</p>
  <p class="brand__tagline centered">Tarrow Guidance Alliance</p>
  <h1 class="event-title centered">Tarrow Flow &amp; Hum<br>Unwind Session</h1>
  <p class="event-mix centered">Bayline Mix</p>
  <p class="event-date centered">Wednesday<br>April 20 | 7PM - 9PM</p>
  <p class="location-label">Event Location</p>
  <p class="location-name">Reedhall at Cobbleyard</p>
</section>

<section class="flyer flyer--square" aria-label="Square flyer">
  <div class="flyer__photo" role="img" aria-label="Photo: sound healer playing a gong in a warmly lit room with participants resting on mats"></div>
  <p class="brand__name centered">Tarrow</p>
  <p class="brand__tagline centered">Tarrow Guidance Alliance</p>
  <h1 class="event-title centered">Tarrow Flow &amp; Hum<br>Unwind Session</h1>
  <p class="event-mix centered">Bayline Mix</p>
  <p class="event-date centered">Wednesday April 20 | 7PM - 9PM</p>
  <p class="location-label">Event Location</p>
  <p class="location-name">Reedhall at Cobbleyard</p>
</section>

</body>
</html>
```